Breezeway Comfort business cards design

Need a business card design for a Heating and Air Conditioning business. I need these items included.
Business name: Breezeway Comfort
Owner: Marcus Tollefsen
License # 2874590
Phone number # 555-382-4071
Email: breezewaycomfortair@mailvista.example
Sales
Service
Installation
Maintenance

Heating and Air Conditioning

Requirements
Must have
• Company name , license number , phone number , email

```html
<!DOCTYPE html>
<html lang="en">
<head>
<meta charset="UTF-8">
<title>Breezeway Comfort – Business Cards</title>
<link href="https://fonts.googleapis.com/css2?family=Roboto:wght@400;700&display=swap" rel="stylesheet">
<style>
  :root {
    --page-bg: #ffffff;
    --card-bg: #eef0f0;
    --frame-white: #ffffff;
    --brand-blue: #1a3be6;
    --contact-pink: #e8256a;
    --warm-orange: #f26522;
    --cool-blue: #2563eb;
  }
  * { margin: 0; padding: 0; box-sizing: border-box; }
  html, body {
    width: 1040px; height: 1200px; overflow: hidden;
    background: var(--page-bg);
    font-family: "Roboto", Arial, sans-serif;
  }
  .canvas { position: relative; width: 1040px; height: 1200px; }

  .card-frame {
    position: absolute; left: 73px; top: 598px;
    width: 900px; height: 540px;
    background: var(--frame-white);
    border: 1px solid #dde2e2;
  }
  .card {
    position: absolute;
    width: 840px; height: 482px;
    background: var(--card-bg);
  }
  .card--front { left: 104px; top: 68px; }
  .card--framed { left: 103px; top: 626px; }

  .owner-name {
    position: absolute; left: 40px; top: 70px;
    font-size: 38px; font-weight: 700; color: var(--brand-blue);
    line-height: 1;
  }
  .owner-title {
    position: absolute; left: 40px; top: 113px;
    font-size: 29px; font-weight: 400; color: var(--brand-blue);
    line-height: 1;
  }
  .brand {
    position: absolute; right: 50px; top: 68px;
    display: flex; align-items: center; gap: 12px;
  }
  .brand-dot {
    width: 34px; height: 34px; border-radius: 50%;
    background: var(--warm-orange);
  }
  .brand-name {
    font-size: 34px; font-weight: 700; color: var(--brand-blue);
    line-height: 1;
  }
  .divider {
    position: absolute; left: 40px; top: 222px;
    width: 750px; height: 8px;
    background: linear-gradient(90deg, var(--warm-orange), var(--cool-blue));
  }
  .contact {
    position: absolute; left: 40px; top: 290px;
    list-style: none;
    font-size: 24px; color: var(--contact-pink);
    line-height: 40px;
  }
  .services {
    position: absolute; left: 0; right: 0; top: 418px;
    text-align: center;
    font-size: 32px; color: var(--brand-blue);
    line-height: 1;
  }
</style>
</head>
<body>
<div class="canvas">

  <section class="card card--front">
    <h1 class="owner-name">Marcus Tollefsen</h1>
    <p class="owner-title">Owner</p>
    <div class="brand"><span class="brand-dot"></span><span class="brand-name">Breezeway Comfort</span></div>
    <div class="divider"></div>
    <ul class="contact">
      <li>License # 2874590</li>
      <li>Phone number # 555-382-4071</li>
      <li>Email: breezewaycomfortair@mailvista.example</li>
    </ul>
    <p class="services">Sales | Service | Installation | Maintenance</p>
  </section>

  <div class="card-frame"></div>
  <section class="card card--framed">
    <h1 class="owner-name">Marcus Tollefsen</h1>
    <p class="owner-title">Owner</p>
    <div class="brand"><span class="brand-dot"></span><span class="brand-name">Breezeway Comfort</span></div>
    <div class="divider"></div>
    <ul class="contact">
      <li>License # 2874590</li>
      <li>Phone number # 555-382-4071</li>
      <li>Email: breezewaycomfortair@mailvista.example</li>
    </ul>
    <p class="services">Sales | Service | Installation | Maintenance</p>
  </section>

</div>
</body>
</html>
```